New Business Card Design Project

I would like my card design to look exactly like the logo, design, layout, and print of the current attached file. The only change I would like made would be for the print to say THE KMW GROUP instead of THE HALLORAN GROUP. Basically, just replace his group name with my group name. I would also like the backgroud to be the same texture and color as the attached file. I love the dark blue lettering and house logo on the card.

I am completely open to the rest of the card design. I just want something clean and simple. Only basic contact info required on the card. Maybe just name: Kyle M Warrick and cell # 555.914.2087 and email kyle@orchidhomesagent.com

```html
<!DOCTYPE html>
<html lang="en">
<head>
<meta charset="UTF-8">
<title>The KMW Group – Business Card</title>
<link rel="stylesheet" href="https://fonts.googleapis.com/css2?family=Jost:wght@400;500&display=swap">
<style>
  :root {
    --backdrop: #141414;
    --card-paper: #e6e6e4;
    --card-paper-shade: #d9d9d7;
    --ink-navy: #1f3d78;
    --ink-slate: #364563;
  }
  html, body {
    margin: 0;
    padding: 0;
    width: 1200px;
    height: 927px;
    overflow: hidden;
    background: var(--backdrop);
  }
  .canvas {
    position: relative;
    width: 1200px;
    height: 927px;
  }
  .business-card {
    position: absolute;
    left: 150px;
    top: 206px;
    width: 900px;
    height: 514px;
    background: radial-gradient(ellipse at 40% 35%, var(--card-paper) 0%, var(--card-paper-shade) 100%);
    font-family: "Jost", "Futura", sans-serif;
    color: var(--ink-slate);
  }
  .brand-lockup {
    position: absolute;
    left: 110px;
    top: 205px;
    display: flex;
    align-items: center;
    gap: 30px;
  }
  .brand-square {
    width: 18px;
    height: 18px;
    background: var(--ink-navy);
  }
  .brand-name {
    margin: 0;
    font-weight: 400;
    font-size: 30px;
    line-height: 1.18;
    letter-spacing: 0.28em;
    color: var(--ink-slate);
  }
  .contact-block {
    position: absolute;
    left: 470px;
    top: 168px;
  }
  .contact-name {
    margin: 0 0 14px;
    font-weight: 400;
    font-size: 36px;
    color: var(--ink-slate);
  }
  .contact-list {
    list-style: none;
    margin: 0;
    padding: 0;
  }
  .contact-item {
    display: flex;
    align-items: center;
    gap: 12px;
    font-size: 29px;
    line-height: 1.35;
    color: var(--ink-slate);
  }
  .contact-icon {
    width: 20px;
    height: 20px;
    flex: none;
  }
</style>
</head>
<body>
<main class="canvas">
  <section class="business-card" aria-label="Business card for The KMW Group">
    <div class="brand-lockup">
      <span class="brand-square" aria-hidden="true"></span>
      <p class="brand-name">THE<br>KMW<br>GROUP</p>
    </div>

    <div class="contact-block">
      <h1 class="contact-name">Kyle M Warrick</h1>
      <ul class="contact-list">
        <li class="contact-item">
          <svg class="contact-icon" viewBox="0 0 20 20" aria-hidden="true">
            <circle cx="10" cy="10" r="9" fill="var(--ink-navy)"/>
            <path d="M7 5.5 L8.6 5.5 L9.3 8 L8.2 8.9 Q9.2 11 11.1 11.8 L12 10.7 L14.5 11.4 L14.5 13 Q13.5 14.5 11.5 14 Q7 12.5 6 8 Q5.6 6 7 5.5 Z" fill="var(--card-paper)"/>
          </svg>
          <span>555 914 2087</span>
        </li>
        <li class="contact-item">
          <svg class="contact-icon" viewBox="0 0 20 20" aria-hidden="true">
            <circle cx="10" cy="10" r="9" fill="var(--ink-navy)"/>
            <rect x="5" y="6.5" width="10" height="7" fill="var(--card-paper)"/>
            <path d="M5 6.5 L10 10.5 L15 6.5" fill="none" stroke="var(--ink-navy)" stroke-width="1"/>
          </svg>
          <span>kyle@orchidhomesagent.com</span>
        </li>
      </ul>
    </div>
  </section>
</main>
</body>
</html>
```